Oil and Gas Letterhead Design Tweak

Simple letterhead information and design tweak.

Please note, we don't want to change the design or logo of the letterhead only the small changes mentioned below.

We need to change the company name up top to "Northvale Petrotek FZCO"

Also, we need to include in the footer the following information. I have attached an image of roughly how we would like to have it displayed in the footer.

Footer Details:

Northvale Petrotek FZCO,
Unit No. 2378, FZCO Trade Hub, level No. 1, K&P 7, Dubai, United Arab Emirates
Northvale Petrotek FZCO is registered as a free zone company under the rules & regulations of FZCO

Target Market(s)

O&G Market

Industry/Entity Type

Oil And Gas

Font styles to use
Sans Serif

Colors

Designer to choose colors to be used in the design.

Requirements
Must have
• Change the company name to Northvale Petrotek FZCO
• Include the footer on the bottom of the first and continuation page
Should not have
• Should not change the design or logo of the letterhead, only the specified changes mentioned above

```html
<!DOCTYPE html>
<html lang="en">
<head>
<meta charset="utf-8">
<title>Northvale Petrotek FZCO — Letterhead</title>
<link href="https://fonts.googleapis.com/css2?family=Open+Sans:wght@400;600;700&display=swap" rel="stylesheet">
<style>
  :root {
    --brand-blue: #1257a6;
    --brand-red: #e31e26;
    --paper: #fdfdfd;
    --ink: #1a1a1a;
    --muted: #4a4a4a;
    --trim: #555555;
  }
  html, body {
    margin: 0;
    padding: 0;
    overflow: hidden;
    background: var(--paper);
  }
  .letterhead {
    position: relative;
    width: 930px;
    height: 1200px;
    background: var(--paper);
    overflow: hidden;
    font-family: "Open Sans", Arial, sans-serif;
  }
  .letterhead__art {
    position: absolute;
    inset: 0;
  }
  .company-title {
    position: absolute;
    left: 110px;
    top: 92px;
    margin: 0;
    font-size: 20px;
    font-weight: 700;
    letter-spacing: 0.6px;
    line-height: 24px;
    color: var(--brand-blue);
    text-transform: uppercase;
  }
  .brand-lockup {
    position: absolute;
    left: 542px;
    width: 280px;
    top: 1018px;
    text-align: center;
    font-weight: 600;
    font-size: 8px;
    line-height: 9px;
    letter-spacing: 0.1px;
    color: var(--ink);
    text-transform: uppercase;
  }
  .brand-lockup__mark {
    display: block;
    width: 14px;
    height: 14px;
    margin: 0 auto 6px;
    background: var(--brand-blue);
  }
  .brand-lockup__name {
    display: block;
  }
  .footer-details {
    position: absolute;
    left: 100px;
    top: 1108px;
    width: 720px;
    margin: 0;
    font-size: 8.5px;
    line-height: 12px;
    color: var(--muted);
    font-style: normal;
  }
  .footer-details__company {
    display: block;
    font-weight: 700;
    color: var(--brand-blue);
  }
  .footer-details__line {
    display: block;
  }
</style>
</head>
<body>
  <main class="letterhead">
    <svg class="letterhead__art" width="930" height="1200" viewBox="0 0 930 1200" aria-hidden="true">
      <g class="trim-marks" stroke="var(--trim)" stroke-width="0.8" fill="none">
        <path d="M103 89 V96 H96"/>
        <path d="M814 89 V96 H821"/>
      </g>
      <g class="header-accent">
        <polygon points="620,88 689,88 675,115 634,115" fill="var(--brand-blue)"/>
        <polygon points="696,88 738,88 726,115 682,115" fill="var(--brand-red)"/>
      </g>
      <g class="footer-bands">
        <polygon points="100,1080 635,1080 624,1102 100,1102" fill="var(--brand-blue)"/>
        <polygon points="727,1073 822,1073 822,1102 744,1102" fill="var(--brand-red)"/>
      </g>
    </svg>

    <h1 class="company-title">Northvale Petrotek FZCO</h1>

    <div class="brand-lockup">
      <span class="brand-lockup__mark"></span>
      <span class="brand-lockup__name">Northvale Petrotek</span>
      <span class="brand-lockup__name">Northvale Petrotek FZCO</span>
    </div>

    <address class="footer-details">
      <span class="footer-details__company">Northvale Petrotek FZCO,</span>
      <span class="footer-details__line">Unit No. 2378, FZCO Trade Hub, level No. 1, K&amp;P 7, Dubai, United Arab Emirates</span>
      <span class="footer-details__line">Northvale Petrotek FZCO is registered as a free zone company under the rules &amp; regulations of FZCO</span>
    </address>
  </main>
</body>
</html>
```